Brimble Diecast Torvel Collectables Website

looking for a vibrant web site marketplace built for diecast car enthusiasts to buy, sell, and trade with ease. Whether you're looking to showcase your own collection or discover rare and exciting models, our site makes the process simple and enjoyable. Clients can browse a curated inventory of high‑quality diecast cars, connect with fellow collectors, and find the perfect pieces to expand their collection. With a smooth user experience and a community-driven spirit, we’re the go‑to destination for anyone passionate about diecast cars.

Target Market(s)

diecast collectors

Industry/Entity Type

Diecast Collectables

Coding

Coded - Design and coding required

Number of Pages Required

3 page

Font styles to use
Sans Serif

Colors
EE7325
F08F49
F5BC92
FAE3D3
FDF4ED

Requirements
Must have
• Cool look and feel. Woo commerce page to post and sell my inventory
Nice to have
• page for users to post their cars or looking for trades.
Should not have
• look cheap

```html
<!DOCTYPE html>
<html lang="en">
<head>
<meta charset="utf-8">
<title>Brimble Diecast — Website Pages</title>
<link href="https://fonts.googleapis.com/css2?family=Plus+Jakarta+Sans:wght@400;500;600;700;800&display=swap" rel="stylesheet">
<style>
:root{
  --orange:#EE7325;
  --orange-soft:#F08F49;
  --peach:#F5BC92;
  --cream:#FAE3D3;
  --ivory:#FDF4ED;
  --rust:#B4520F;
  --board:#B4521A;
  --ink:#1d1a18;
  --muted:#7a716b;
  --line:#eadfd6;
  --footer:#F3F1EF;
}
*{box-sizing:border-box;margin:0;padding:0}
html,body{width:1200px;height:1200px;overflow:hidden;background:var(--board)}
body{font-family:"Plus Jakarta Sans",Arial,sans-serif;color:var(--ink)}
.board{position:absolute;left:0;top:0;width:1932px;height:1932px;transform:scale(.62112);transform-origin:0 0;background:var(--board)}
.page-title{position:absolute;top:103px;height:30px;width:395px;background:#fff;font-weight:700;font-size:21px;display:flex;align-items:center;justify-content:center;letter-spacing:-.3px}
.page{position:absolute;top:158px;width:395px;background:#fff;overflow:hidden}
.a{position:absolute}
.nav{position:absolute;left:0;top:0;width:395px;height:32px;background:var(--ivory);display:flex;align-items:center;font-size:4.6px}
.nav .brand{position:absolute;left:8px;font-weight:700;font-size:5px;color:var(--rust)}
.nav .links{position:absolute;left:42px;display:flex;gap:11px;color:#444}
.nav .links .on{color:var(--rust);border-bottom:1px solid var(--rust);padding-bottom:2px}
.nav .search{position:absolute;left:232px;width:78px;height:11px;border-radius:6px;background:#f3ebe4;color:#aaa;font-size:3.8px;padding-left:12px;line-height:11px}
.nav .search::before{content:"";position:absolute;left:4px;top:3px;width:4px;height:4px;border:.7px solid #999;border-radius:50%}
.nav .icons{position:absolute;left:316px;display:flex;gap:4px}
.nav .icons i{width:5px;height:6px;border:.8px solid #333;border-radius:1px;display:block}
.nav .cta{position:absolute;left:342px;width:43px;height:9px;border-radius:5px;background:var(--rust);color:#fff;font-size:3.8px;text-align:center;line-height:9px;font-weight:600}
.badge{display:inline-block;background:var(--cream);color:var(--rust);font-size:3.5px;font-weight:700;letter-spacing:.4px;padding:2px 4px;border-radius:2px;line-height:1.2}
.label{font-size:3.4px;letter-spacing:.5px;color:var(--rust);font-weight:700;text-transform:uppercase}
.h-hero{font-weight:700;letter-spacing:-.6px;line-height:1.05}
.h-hero em{font-style:normal;color:var(--rust)}
.txt{font-size:4.4px;line-height:1.6;color:var(--muted)}
.small{font-size:3.5px;line-height:1.5;color:var(--muted)}
.btn{display:inline-flex;align-items:center;justify-content:center;border-radius:10px;font-size:4.6px;font-weight:600;height:19px;padding:0 12px;white-space:nowrap}
.btn.primary{background:var(--rust);color:#fff;box-shadow:0 2px 4px rgba(180,82,15,.3)}
.btn.ghost{background:#fff;border:.8px solid var(--line);color:var(--ink)}
.photo{position:absolute;border-radius:4px}
.card{position:absolute;background:#fff;border-radius:4px;box-shadow:0 3px 10px rgba(120,60,20,.12)}
.price{font-weight:700;color:var(--rust)}
.sec-h{font-weight:600;letter-spacing:-.3px;text-align:center}
.ph-studio{background:linear-gradient(160deg,#f3f1ef,#d9d6d3)}
.ph-red{background:radial-gradient(ellipse at 50% 55%,#c62828 0 18%,#ecebea 40%,#d2d0ce)}
.ph-dark{background:radial-gradient(ellipse at 50% 60%,#b71c1c 0 16%,#3a3a3a 40%,#151515)}
.ph-blue{background:radial-gradient(ellipse at 45% 45%,#1f6fcc 0 28%,#6c6f73 55%,#3d3f42)}
.ph-yellow{background:radial-gradient(ellipse at 50% 50%,#f2c20b 0 25%,#f2f2f2 45%,#e6e6e6)}
.ph-silver{background:radial-gradient(ellipse at 50% 55%,#cfd2d6 0 25%,#5b5e63 50%,#2a2c2f)}
.ph-gray{background:linear-gradient(160deg,#3c3c3c,#191919)}
.ph-orange{background:radial-gradient(ellipse at 55% 55%,#f07b12 0 16%,#eeeeee 40%,#d8d8d8)}
.ph-wood{background:linear-gradient(180deg,#6d4a2c,#c69a68 60%,#a67a4c)}
.ph-engine{background:radial-gradient(ellipse at 50% 50%,#c9c9c9 0 30%,#2f2f2f 70%)}
.ph-green{background:radial-gradient(ellipse at 50% 60%,#1e5a42 0 22%,#c9c9c9 45%,#b0b0b0)}
.ph-person{background:linear-gradient(160deg,#5a534d,#1e1c1b)}
.ph-classic{background:radial-gradient(ellipse at 50% 55%,#7b1b1b 0 20%,#f3f3f3 45%,#e3e3e3)}
.feat{position:absolute;width:110px;text-align:center}
.feat .ico{width:18px;height:18px;border-radius:50%;background:var(--cream);margin:0 auto 8px;display:flex;align-items:center;justify-content:center}
.feat h4{font-size:5.4px;font-weight:600;margin-bottom:5px}
.step{position:absolute;background:#fff;border-radius:4px;padding:8px 8px}
.step .n{font-size:11px;font-weight:700;color:var(--peach)}
.step.on .n{color:var(--rust)}
.step h5{font-size:5px;font-weight:600;margin:4px 0 3px}
.trust{position:absolute;background:#fff;border-radius:4px;text-align:center;padding:10px 5px}
.trust h5{font-size:5px;font-weight:600;margin:3px 0 2px;line-height:1.2}
.footer{position:absolute;left:0;width:395px;height:152px;background:var(--footer)}
.footer .logo{position:absolute;left:10px;top:22px;font-size:5px;font-weight:700;color:var(--rust);display:flex;align-items:center;gap:3px}
.footer .logo span{width:10px;height:10px;border-radius:50%;background:var(--rust);display:block}
.footer .about{position:absolute;left:10px;top:55px;width:72px}
.footer .social{position:absolute;left:10px;top:96px;display:flex;gap:8px}
.footer .social i{width:5px;height:5px;border-radius:50%;background:#333;display:block}
.footer .col{position:absolute;top:28px;font-size:3.8px;color:var(--muted);line-height:12.6px}
.footer .col b{display:block;color:var(--ink);font-weight:600;margin-bottom:2px}
.footer .mail{position:absolute;left:302px;top:36px;width:82px}
.footer .field{margin-top:8px;height:9px;width:68px;border-radius:5px;background:#fff;font-size:3.2px;color:#aaa;line-height:9px;padding-left:4px}
.footer .go{position:absolute;right:0;bottom:0;width:9px;height:9px;border-radius:50%;background:var(--rust)}
.footer .bottom{position:absolute;left:10px;right:10px;top:134px;font-size:3.2px;color:var(--muted);display:flex;justify-content:space-between}
.spec b{display:block;font-size:3px;color:var(--muted);font-weight:500;letter-spacing:.3px}
.spec span{font-size:3.8px;font-weight:600}
.chip{position:absolute;background:#fdf1e8;border-radius:5px;font-size:3.3px;padding:3px 5px;display:flex;gap:3px;align-items:center;line-height:1.3}
.chip i{width:4px;height:4px;border:.6px solid var(--rust);border-radius:1px;display:block}
.input{position:absolute;background:#fbf6f2;border:.6px solid var(--line);border-radius:2px;font-size:3.4px;color:#aaa;padding:3px 4px}
</style>
</head>
<body>
<div class="board">

  <div class="page-title" style="left:153px">Home page</div>
  <div class="page-title" style="left:560px">Brimble Diecast – Marketplace</div>
  <div class="page-title" style="left:974px">Sell &amp; Trade</div>
  <div class="page-title" style="left:1385px">Brimble Diecast – Product Detail</div>

  <!-- HOME -->
  <section class="page" style="left:153px;height:1685px">
    <nav class="nav"><span class="brand">Brimble</span><div class="links"><span>Marketplace</span><span>Sell &amp; Trade</span><span>Community</span></div><div class="search">Search models...</div><div class="icons"><i></i><i style="border-radius:50%"></i></div><div class="cta">List Your Car</div></nav>

    <div class="a" style="left:20px;top:74px"><span class="badge">BEST LIMITED COLLECTION</span></div>
    <h1 class="a h-hero" style="left:20px;top:88px;font-size:20px;width:170px">Buy. Sell. Trade.<br>Collect. — <em>All<br>in One Place</em></h1>
    <p class="a txt" style="left:20px;top:160px;width:170px">Discover rare diecast cars from world-class collectors. A curated marketplace where precision engineering meets the passion of the hunt.</p>
    <div class="a" style="left:20px;top:200px;display:flex;gap:8px"><span class="btn primary">Browse Collection</span><span class="btn ghost">List Your Car</span></div>
    <div class="photo ph-red" role="img" aria-label="Red sports car model on a white studio floor" style="left:208px;top:58px;width:160px;height:110px;box-shadow:0 4px 12px rgba(0,0,0,.12)"></div>
    <div class="card" style="left:215px;top:178px;width:145px;height:52px;padding:7px 8px">
      <div class="label" style="font-weight:500">Featured Arrival</div>
      <div style="font-size:6px;font-weight:600;margin-top:2px">1967 Coastline Fastback</div>
      <div class="small" style="position:absolute;left:8px;bottom:8px">Scale: 1:18 | Limited Edition</div>
      <div style="position:absolute;right:8px;bottom:7px;font-size:5.4px;font-weight:700">$285.00</div>
    </div>

    <div class="a" style="left:0;top:270px;width:395px;height:170px;background:var(--cream)"></div>
    <h2 class="a sec-h" style="left:0;top:295px;width:395px;font-size:11px;line-height:1.45">Where Collectors Connect &amp;<br><span style="border-bottom:1px solid var(--ink)">Collections Grow</span></h2>
    <div class="feat" style="left:27px;top:350px"><div class="ico"><svg width="8" height="8" viewBox="0 0 10 10"><circle cx="5" cy="5" r="4" fill="none" stroke="#B4520F"/><path d="M3 5l1.5 1.5L7 4" stroke="#B4520F" fill="none"/></svg></div><h4>Curated Inventory</h4><p class="small">Every listing is hand-reviewed to ensure authenticity and quality standards are met before going live.</p></div>
    <div class="feat" style="left:143px;top:350px"><div class="ico"><svg width="8" height="8" viewBox="0 0 10 10"><path d="M1 4h7l-2-2M9 6H2l2 2" stroke="#B4520F" fill="none"/></svg></div><h4>Seamless Trading</h4><p class="small">Our proprietary secure trade system allows enthusiasts to swap models with confidence and low fees.</p></div>
    <div class="feat" style="left:259px;top:350px"><div class="ico"><svg width="8" height="8" viewBox="0 0 10 10"><circle cx="3" cy="4" r="1.5" fill="#B4520F"/><circle cx="7" cy="4" r="1.5" fill="#B4520F"/><path d="M0 9q3-4 5 0q2-4 5 0" fill="#B4520F"/></svg></div><h4>Collector Community</h4><p class="small">Join specialized forums and local groups. Share your display setups and find the next piece for your garage.</p></div>

    <h2 class="a" style="left:30px;top:476px;font-size:12px;font-weight:600;letter-spacing:-.3px">Featured Diecast Models</h2>
    <p class="a small" style="left:30px;top:494px;width:160px">The pinnacle of miniature engineering. Explore our most sought-after listings of the week.</p>
    <div class="a" style="left:312px;top:502px;font-size:4px;color:var(--rust);font-weight:600">View Entire Gallery →</div>
    <div class="photo ph-blue" role="img" aria-label="Blue racing sports car model in a garage setting" style="left:30px;top:525px;width:220px;height:182px">
      <div class="a" style="left:10px;top:134px"><span class="badge" style="background:var(--orange);color:#fff">RARE FIND</span></div>
      <div class="a" style="left:10px;top:145px;color:#fff;font-size:7px;font-weight:600">Velocita RS 'Harbor Blue'</div>
      <div class="a" style="left:10px;top:158px;color:#ddd;font-size:3.2px;width:80px">Scale 1:12 | Signature Edition | Mint Condition</div>
      <div class="a" style="right:10px;top:138px;color:#fff;font-size:10px;font-weight:600">$1,250</div>
      <div class="a" style="right:10px;top:156px;background:#fff;border-radius:4px;font-size:3.4px;padding:2px 8px;font-weight:600">Place Bid</div>
    </div>
    <div class="card" style="left:262px;top:530px;width:105px;height:85px;padding:3px">
      <div class="photo ph-classic" role="img" aria-label="Dark red classic muscle car model" style="position:relative;height:50px"></div>
      <div style="font-size:5px;font-weight:500;margin:8px 2px 1px">Classic Marauder 1965</div><div class="small" style="margin-left:2px">1:24 Scale</div>
      <div class="price a" style="right:5px;top:68px;font-size:5.6px">$1,045</div>
    </div>
    <div class="card" style="left:262px;top:623px;width:105px;height:85px;padding:3px">
      <div class="photo" role="img" aria-label="Silver concept hypercar model" style="position:relative;height:50px;background:radial-gradient(ellipse at 50% 55%,#9aa0a6 0 25%,#f2f2f2 55%)"></div>
      <div style="font-size:5px;font-weight:500;margin:8px 2px 1px">Concept Solenne 2023</div><div class="small" style="margin-left:2px">1:18 Scale</div>
      <div class="price a" style="right:5px;top:68px;font-size:5.6px">$310</div>
    </div>

    <div class="a" style="left:0;top:752px;width:395px;height:172px;background:var(--ivory)"></div>
    <div class="card" style="left:30px;top:782px;width:105px;height:115px;padding:10px 12px">
      <div class="a" style="right:6px;top:4px;font-size:15px;font-weight:700;color:#f3ece6">01</div>
      <svg width="10" height="10" viewBox="0 0 10 10"><rect x="1" y="3" width="8" height="7" rx="1" fill="#B4520F"/><path d="M3 3V2a2 2 0 014 0v1" stroke="#B4520F" fill="none"/></svg>
      <div style="font-size:5.6px;font-weight:600;margin:10px 0 5px">Buy Your Grail</div>
      <p class="small">Access an exclusive global marketplace of verified miniature masterpieces. Browse by scale, brand, or era.</p>
      <div style="font-size:3.8px;color:var(--rust);font-weight:600;margin-top:8px">Start Shopping →</div>
    </div>
    <div class="card" style="left:145px;top:782px;width:105px;height:115px;padding:10px 12px">
      <div class="a" style="right:6px;top:4px;font-size:15px;font-weight:700;color:#f3ece6">02</div>
      <svg width="10" height="10" viewBox="0 0 10 10"><path d="M1 1h4l4 4-4 4-4-4z" fill="#B4520F"/></svg>
      <div style="font-size:5.6px;font-weight:600;margin:10px 0 5px">Sell with Ease</div>
      <p class="small">Turn your collection into capital. Reach thousands of serious collectors with our professional listing tools.</p>
      <div style="font-size:3.8px;color:var(--rust);font-weight:600;margin-top:8px">List a Model →</div>
    </div>
    <div class="card" style="left:260px;top:782px;width:105px;height:115px;padding:10px 12px">
      <div class="a" style="right:6px;top:4px;font-size:15px;font-weight:700;color:#f3ece6">03</div>
      <svg width="10" height="10" viewBox="0 0 10 10"><path d="M2 4a3 3 0 015-1l1-1v3H5l1-1a2 2 0 00-3 1M8 6a3 3 0 01-5 1L2 8V5h3L4 6a2 2 0 003-1" fill="#B4520F"/></svg>
      <div style="font-size:5.6px;font-weight:600;margin:10px 0 5px">Trade &amp; Swap</div>
      <p class="small">Trade up or pivot your focus. Securely swap models with other enthusiasts using our escrow protection.</p>
      <div style="font-size:3.8px;color:var(--rust);font-weight:600;margin-top:8px">Explore Trades →</div>
    </div>

    <div class="photo ph-person" role="img" aria-label="Portrait of a collector" style="left:30px;top:988px;width:78px;height:78px"></div>
    <div class="photo ph-person" role="img" aria-label="Portrait of a collector in a suit" style="left:112px;top:973px;width:78px;height:60px"></div>
    <div class="photo ph-person" role="img" aria-label="Portrait of a collector" style="left:30px;top:1072px;width:78px;height:58px"></div>
    <div class="photo ph-person" role="img" aria-label="Portrait of a collector with glasses" style="left:112px;top:1038px;width:78px;height:78px"></div>
    <div class="a label" style="left:204px;top:965px">The Collective</div>
    <h2 class="a" style="left:204px;top:975px;font-size:11.5px;font-weight:600;line-height:1.3;width:140px">More Than a Marketplace — A Community</h2>
    <p class="a txt" style="left:204px;top:1027px;width:160px">Brimble Diecast is built by collectors, for collectors. Join 50,000+ enthusiasts who share detailed photography, host digital garage tours, and meet up for exclusive events.</p>
    <div class="a" style="left:204px;top:1063px;width:160px"><div style="font-size:5px;font-weight:600">▣ Expert Forums</div><p class="small" style="padding-left:9px">Get advice on restoration, valuation, and spotting replicas.</p></div>
    <div class="a" style="left:204px;top:1093px;width:160px"><div style="font-size:5px;font-weight:600">◉ Photo Showcases</div><p class="small" style="padding-left:9px">Upload your professional dioramas and gain community recognition.</p></div>
    <div class="a" style="left:204px;top:1122px"><span class="btn primary" style="height:16px;font-size:3.8px">Join the Community</span></div>

    <div class="a" style="left:0;top:1178px;width:395px;height:182px;background:var(--cream)"></div>
    <h2 class="a sec-h" style="left:0;top:1205px;width:395px;font-size:11.5px">Built on Trust &amp; Quality</h2>
    <p class="a small" style="left:97px;top:1228px;width:200px;text-align:center;font-size:4px">We maintain the highest standards in the industry to ensure your peace of mind with every transaction.</p>
    <div class="trust" style="left:30px;top:1265px;width:75px;height:65px"><svg width="9" height="9" viewBox="0 0 10 10"><rect x="1" y="3" width="8" height="6" rx="1" fill="none" stroke="#B4520F"/><circle cx="5" cy="6" r="1.5" fill="none" stroke="#B4520F"/></svg><h5>High-Res Standards</h5><p class="small">Mandatory 360° views for all premium listings.</p></div>
    <div class="trust" style="left:117px;top:1265px;width:75px;height:65px"><svg width="9" height="9" viewBox="0 0 10 10"><path d="M5 1l4 1.5v3Q9 8 5 9.5Q1 8 1 5.5v-3z" fill="none" stroke="#B4520F"/></svg><h5>Verified Sellers</h5><p class="small">Background checked and rating-verified community.</p></div>
    <div class="trust" style="left:204px;top:1265px;width:75px;height:65px"><svg width="9" height="9" viewBox="0 0 10 10"><rect x="1.5" y="1" width="7" height="8" rx="1" fill="none" stroke="#B4520F"/><path d="M3 4h4M3 6h4" stroke="#B4520F"/></svg><h5>Condition Grading</h5><p class="small">Standardized grading system for objective condition reports.</p></div>
    <div class="trust" style="left:290px;top:1265px;width:75px;height:65px"><svg width="9" height="9" viewBox="0 0 10 10"><rect x="1" y="2" width="8" height="6" rx="1" fill="none" stroke="#B4520F"/><circle cx="5" cy="5" r="1.3" fill="#B4520F"/></svg><h5>Escrow Protection</h5><p class="small">Funds are only released once you've inspected the model.</p></div>

    <div class="a" style="left:30px;top:1368px;width:335px;height:155px;border-radius:10px;background:linear-gradient(160deg,var(--orange),var(--orange-soft) 55%,var(--peach));box-shadow:0 6px 14px rgba(180,82,15,.25)">
      <h2 style="color:#fff;font-size:16px;font-weight:700;text-align:center;line-height:1.15;margin-top:30px">Start Building Your Dream<br>Collection Today</h2>
      <p style="color:#fff;opacity:.85;font-size:4.6px;text-align:center;width:180px;margin:8px auto 0;line-height:1.5">Join the world's most sophisticated diecast marketplace and find that missing piece.</p>
      <div style="display:flex;gap:6px;justify-content:center;margin-top:12px"><span class="btn" style="background:#fff;color:var(--rust)">Get Started Now</span><span class="btn" style="background:#c8611f;color:#fff">Learn More</span></div>
    </div>

    <footer class="footer" style="top:1533px">
      <div class="logo"><span></span>Brimble Diecast</div>
      <p class="about small">Your Marketplace for Miniature Masterpieces. Connecting collectors across the globe since 2024.</p>
      <div class="social"><i></i><i></i><i></i></div>
      <div class="col" style="left:108px"><b>Quick Links</b>Browse Collection<br>Sell Your Cars<br>Trade Portal<br>Community Forum<br>Newsletter</div>
      <div class="col" style="left:205px"><b>Resources</b>FAQ<br>Contact Support<br>Terms of Service<br>Privacy Policy<br>Grading Guide</div>
      <div class="a" style="left:302px;top:28px;font-size:3.8px;font-weight:600">Join the Mailing List</div>
      <div class="mail"><p class="small">Receive weekly rare find alerts and community auction highlights.</p><div class="field">email@address.com</div><span class="go"></span></div>
      <div class="bottom"><span>© 2026 Brimble Diecast. Your Marketplace for Miniature Masterpieces.</span><span>LONDON &nbsp;•&nbsp; TOKYO &nbsp;•&nbsp; NEW YORK</span></div>
    </footer>
  </section>

  <!-- MARKETPLACE -->
  <section class="page" style="left:560px;height:832px">
    <nav class="nav"><span class="brand">Brimble</span><div class="links"><span class="on">Marketplace</span><span>Sell &amp; Trade</span><span>Community</span></div><div class="search">Search models...</div><div class="icons"><i></i><i style="border-radius:50%"></i></div><div class="cta">List Your Car</div></nav>
    <div class="a" style="left:0;top:32px;width:395px;height:240px;background:linear-gradient(180deg,#fff,var(--ivory))"></div>
    <div class="a" style="left:20px;top:88px"><span class="badge">LIMITED COLLECTION</span></div>
    <h1 class="a h-hero" style="left:20px;top:104px;font-size:20px">The Curated<br><em>Archive.</em></h1>
    <p class="a txt" style="left:20px;top:152px;width:140px">Discover ultra-rare 1:18 engineering marvels from the world's most prestigious manufacturers.</p>
    <div class="a" style="left:20px;top:183px;display:flex;gap:5px"><span class="btn primary">Shop New Arrivals</span><span class="btn ghost">View Lookbook</span></div>
    <div class="photo ph-dark" role="img" aria-label="Red supercar model on a dark background" style="left:212px;top:64px;width:158px;height:165px;transform:rotate(2deg);box-shadow:0 6px 14px rgba(0,0,0,.25)"></div>
    <div class="card" style="left:218px;top:178px;width:146px;height:55px;padding:6px 8px;transform:rotate(2deg)">
      <div class="label" style="font-weight:500">Featured Arrival</div>
      <div style="font-size:6px;font-weight:600;margin-top:2px;width:90px;line-height:1.25">Aurelio V8 Scarlet Edition</div>
      <div class="small" style="position:absolute;left:8px;bottom:7px">Scale: 1:18 | Limited Edition</div>
      <div style="position:absolute;right:8px;bottom:7px;font-size:5.4px;font-weight:700">$285.00</div>
    </div>

    <div class="a" style="left:22px;top:283px;width:80px">
      <div style="font-size:5.4px;font-weight:600">Filters</div>
      <div class="small" style="margin-top:8px;font-weight:600">SCALE</div>
      <div style="display:flex;gap:3px;margin-top:3px;font-size:3.6px"><span style="background:var(--rust);color:#fff;padding:2px 7px;border-radius:2px">1:18</span><span style="background:var(--cream);padding:2px 5px;border-radius:2px">1:24</span><span style="background:var(--cream);padding:2px 5px;border-radius:2px">1:43</span></div>
      <div class="small" style="margin-top:9px;font-weight:600">BRAND</div>
      <div class="small" style="line-height:2.3">○ Velmont<br>○ Northgate Models<br>○ Saraku<br>○ Fenwick</div>
      <div class="small" style="margin-top:4px;font-weight:600">RARITY</div>
      <div class="small" style="line-height:2.3">○ Common<br>○ Rare Finds<br>○ Grail Status</div>
      <div class="small" style="margin-top:4px;font-weight:600">PRICE RANGE</div>
      <div class="small" style="display:flex;justify-content:space-between;margin-top:8px"><span>$50</span><span>$2,500+</span></div>
    </div>
    <h2 class="a" style="left:117px;top:283px;font-size:9px;font-weight:600">Rare Finds</h2>
    <div class="a" style="left:350px;top:287px;font-size:3.4px;color:var(--rust);font-weight:600">VIEW ALL</div>
    <div class="photo ph-yellow" role="img" aria-label="Yellow supercar model seen from above" style="left:117px;top:303px;width:120px;height:124px;border-radius:2px"><span class="badge a" style="left:8px;top:6px;background:var(--rust);color:#fff">GRAIL</span><span class="a small" style="left:34px;top:7px;color:#333">MINT</span></div>
    <div class="photo ph-silver" role="img" aria-label="Silver classic sports car model" style="left:250px;top:303px;width:122px;height:124px;border-radius:2px"><span class="badge a" style="left:8px;top:6px;background:var(--rust);color:#fff">VINTAGE</span><span class="badge a" style="left:36px;top:6px;background:#333;color:#fff">NEAR MINT</span></div>
    <div class="a" style="left:127px;top:437px;width:110px"><div class="label" style="font-size:3px">Northgate Models • 1:18</div><div style="font-size:6px;font-weight:500;margin-top:3px;width:70px;line-height:1.3">Aurelio V8 Scarlet Edition</div><div class="a" style="right:0;top:0;font-size:7px;font-weight:500">$845.00</div>
      <div class="spec" style="display:flex;gap:18px;margin-top:14px"><div><b>CONDITION</b><span>10/10 Mint</span></div><div><b>RELEASE</b><span>Ltd. 250pcs</span></div></div></div>
    <div class="a" style="left:257px;top:437px;width:113px"><div class="label" style="font-size:3px">Velmont • 1:18</div><div style="font-size:6px;font-weight:500;margin-top:3px;width:70px;line-height:1.3">Hollis Sprint RS Coupe</div><div class="a" style="right:0;top:0;font-size:7px;font-weight:500">$1,250.00</div>
      <div class="spec" style="display:flex;gap:18px;margin-top:14px"><div><b>CONDITION</b><span>9.5/10</span></div><div><b>RARITY</b><span>Extremely Rare</span></div></div></div>

    <h2 class="a" style="left:117px;top:516px;font-size:9px;font-weight:600">Recently Added</h2>
    <div class="a" style="left:345px;top:516px;font-size:6px">‹ &nbsp;&nbsp; ›</div>
    <div class="photo" role="img" aria-label="Silver supercar model on dark floor" style="left:122px;top:543px;width:75px;height:78px;background:radial-gradient(ellipse at 50% 55%,#bdbdbd 0 20%,#2c2c2c 55%)"></div>
    <div class="photo" role="img" aria-label="Blue racing coupe model on dark floor" style="left:208px;top:543px;width:75px;height:78px;background:radial-gradient(ellipse at 50% 55%,#2b7fc4 0 20%,#2c2c2c 55%)"></div>
    <div class="photo" role="img" aria-label="White supercar model on dark floor" style="left:295px;top:543px;width:75px;height:78px;background:radial-gradient(ellipse at 50% 55%,#f0f0f0 0 20%,#2c2c2c 55%)"></div>
    <div class="a" style="left:122px;top:630px;width:75px"><div class="small" style="font-size:3px">SARAKU</div><div style="font-size:4.2px;font-weight:600">Corvane Tempesta LX5</div><div style="font-size:5.4px;font-weight:500;margin-top:3px">$320.00</div></div>
    <div class="a" style="left:208px;top:630px;width:75px"><div class="small" style="font-size:3px">PETITE GRID</div><div style="font-size:4.2px;font-weight:600">Osterwald K4 Sport Evolution</div><div style="font-size:5.4px;font-weight:500;margin-top:3px">$185.00</div></div>
    <div class="a" style="left:295px;top:630px;width:75px"><div class="small" style="font-size:3px">EMBER SCALE</div><div style="font-size:4.2px;font-weight:600">Ryuzen Tempo GTX</div><div style="font-size:5.4px;font-weight:500;margin-top:3px">$495.00</div></div>

    <footer class="footer" style="top:680px">
      <div class="logo"><span></span>Brimble Diecast</div>
      <p class="about small">Your Marketplace for Miniature Masterpieces. Connecting collectors across the globe since 2024.</p>
      <div class="social"><i></i><i></i><i></i></div>
      <div class="col" style="left:108px"><b>Quick Links</b>Browse Collection<br>Sell Your Cars<br>Trade Portal<br>Community Forum<br>Newsletter</div>
      <div class="col" style="left:205px"><b>Resources</b>FAQ<br>Contact Support<br>Terms of Service<br>Privacy Policy<br>Grading Guide</div>
      <div class="a" style="left:302px;top:28px;font-size:3.8px;font-weight:600">Join the Mailing List</div>
      <div class="mail"><p class="small">Receive weekly rare find alerts and community auction highlights.</p><div class="field">email@address.com</div><span class="go"></span></div>
      <div class="bottom"><span>© 2026 Brimble Diecast. Your Marketplace for Miniature Masterpieces.</span><span>LONDON &nbsp;•&nbsp; TOKYO &nbsp;•&nbsp; NEW YORK</span></div>
    </footer>
  </section>

  <!-- SELL & TRADE -->
  <section class="page" style="left:974px;height:1089px">
    <nav class="nav"><span class="brand">Brimble</span><div class="links"><span>Marketplace</span><span class="on">Sell &amp; Trade</span><span>Community</span></div><div class="search">Search models...</div><div class="icons"><i></i><i style="border-radius:50%"></i></div><div class="cta">List Your Car</div></nav>
    <div class="a" style="left:20px;top:78px"><span class="badge">COLLECTOR'S PORTAL</span></div>
    <h1 class="a h-hero" style="left:20px;top:95px;font-size:20px">Sell or Trade<br>Your <em>Diecast<br>Cars</em></h1>
    <p class="a txt" style="left:20px;top:164px;width:140px">Discover ultra-rare 1:18 engineering marvels from the world's most prestigious manufacturers.</p>
    <div class="a" style="left:20px;top:193px;display:flex;gap:5px"><span class="btn primary">List Your Car</span><span class="btn ghost">How it Works</span></div>
    <div class="a" style="left:198px;top:60px;width:172px;height:162px;border:.8px solid var(--peach);border-radius:6px;transform:rotate(-3deg)"></div>
    <div class="photo ph-orange" role="img" aria-label="Orange supercar model on white studio backdrop" style="left:205px;top:68px;width:160px;height:155px;box-shadow:0 5px 12px rgba(0,0,0,.12)"></div>

    <div class="a" style="left:22px;top:268px;width:351px;height:150px;background:var(--cream)"></div>
    <h2 class="a sec-h" style="left:22px;top:295px;width:351px;font-size:11px">The Curated Listing Process</h2>
    <div class="step" style="left:42px;top:318px;width:73px;height:72px"><div class="n">01</div><h5>Create Listing</h5><p class="small" style="font-size:3px">Input the precise scale, make, and manufacturer year. Our database auto-fills specs.</p></div>
    <div class="step on" style="left:122px;top:318px;width:73px;height:72px;border-top:1.5px solid var(--rust)"><div class="n">02</div><h5>Upload Images</h5><p class="small" style="font-size:3px">High-fidelity photography is essential. Use our guide to capture every angle.</p></div>
    <div class="step" style="left:202px;top:318px;width:73px;height:72px"><div class="n">03</div><h5>Connect Buyers</h5><p class="small" style="font-size:3px">Direct encrypted messaging with verified collectors who share your passion.</p></div>
    <div class="step" style="left:282px;top:318px;width:73px;height:72px"><div class="n">04</div><h5>Complete Deal</h5><p class="small" style="font-size:3px">Finalize your transaction with secure payment holding or structured trade terms.</p></div>

    <div class="card" style="left:85px;top:430px;width:225px;height:325px">
      <div class="a" style="left:17px;top:16px;font-size:8px;font-weight:600">Listing Details</div>
      <div class="a small" style="left:17px;top:28px">Complete the specification sheet for your miniature masterpiece.</div>
      <div class="a" style="left:17px;top:44px;width:192px;height:104px;background:var(--ivory);border:.6px solid var(--peach);border-radius:2px;text-align:center;padding-top:40px">
        <svg width="12" height="10" viewBox="0 0 12 10"><rect x="1" y="2" width="10" height="7" rx="1" fill="none" stroke="#B4520F"/><circle cx="6" cy="5.5" r="2" fill="none" stroke="#B4520F"/></svg>
        <div style="font-size:3.6px;font-weight:600">Drag and drop high-res images</div><div class="small" style="font-size:3px">Recommended: 2000 × 1500px, PNG or JPG</div>
      </div>
      <div class="a small" style="left:17px;top:157px;font-weight:600;font-size:3.2px">MODEL TITLE</div>
      <div class="input" style="left:17px;top:165px;width:92px">e.g. 1967 Coastline Roadster</div>
      <div class="a small" style="left:117px;top:157px;font-weight:600;font-size:3.2px">SCALE &amp; MAKE</div>
      <div class="input" style="left:117px;top:165px;width:92px">1:18 Scale ▾</div>
      <div class="a small" style="left:17px;top:187px;font-weight:600;font-size:3.2px">DETAILED DESCRIPTION</div>
      <div class="input" style="left:17px;top:195px;width:192px;height:42px">Describe the condition, paint finish, and any limited edition numbering...</div>
      <div class="a" style="left:17px;top:248px;width:192px;height:24px;background:var(--ivory);border-radius:2px"></div>
      <div class="a" style="left:25px;top:254px;font-size:3.2px;display:flex;gap:8px;align-items:center"><span style="background:var(--rust);color:#fff;padding:2px 6px;border-radius:4px">For Sale</span><span>Trade Only</span><span style="width:7px;height:7px;border:.6px solid #999;border-radius:50%;display:inline-block"></span></div>
      <div class="input" style="left:148px;top:254px;width:55px;background:#fff">$ 0.00</div>
      <div class="a" style="left:17px;top:288px;display:flex;gap:5px"><span class="btn primary" style="height:11px;font-size:3.2px;padding:0 14px">Create Marketplace Listing</span><span class="btn ghost" style="height:11px;font-size:3.2px">Save Draft</span></div>
    </div>

    <div class="a" style="left:32px;top:828px;width:103px;height:73px;background:linear-gradient(160deg,var(--rust),#9c440c);border-radius:4px;padding:9px;color:#fff">
      <svg width="9" height="9" viewBox="0 0 10 10"><circle cx="5" cy="5" r="4.5" fill="#fff"/><path d="M3 5l1.5 1.5L7 4" stroke="#B4520F" fill="none"/></svg>
      <div style="font-size:5px;font-weight:600;margin-top:2px;line-height:1.2">Authenticity<br>Guaranteed</div>
      <p style="font-size:3px;line-height:1.5;opacity:.85;margin-top:2px">All high-value trades undergo a secondary verification process to ensure scale and condition accuracy for both parties.</p>
    </div>
    <div class="a" style="left:145px;top:790px;width:102px;height:50px;background:var(--cream);border-radius:3px;padding:8px"><div class="label" style="font-size:3px;color:var(--muted)">Listing Perk</div><div style="font-size:5px;font-weight:600;margin:2px 0">Global Reach</div><p class="small" style="font-size:3px">Access over 50,000 active collectors from Tokyo to New York within minutes of posting.</p></div>
    <div class="a" style="left:258px;top:790px;width:105px;height:50px;background:var(--cream);border-radius:3px;padding:8px"><div class="label" style="font-size:3px;color:var(--muted)">Trade Flow</div><div style="font-size:5px;font-weight:600;margin:2px 0">Secure Escrow</div><p class="small" style="font-size:3px">Our system holds payments and tracks shipping until both collectors confirm receipt.</p></div>
    <div class="a" style="left:145px;top:848px;width:218px;height:52px;background:var(--cream);border-radius:3px"></div>
    <div class="photo" role="img" aria-label="Model car in a dimly lit display case" style="left:152px;top:856px;width:38px;height:36px;border-radius:2px;background:radial-gradient(ellipse at 50% 60%,#d89a3c 0 15%,#1d1d1d 55%)"></div>
    <div class="a" style="left:196px;top:862px;width:160px"><div style="font-size:5px;font-weight:600">Technical Perfection</div><p class="small" style="font-size:3px">Our digital condition tool scans your photos to suggest condition grades (Mint, Near Mint, or Display-Grade) automatically.</p></div>

    <footer class="footer" style="top:937px">
      <div class="logo"><span></span>Brimble Diecast</div>
      <p class="about small">Your Marketplace for Miniature Masterpieces. Connecting collectors across the globe since 2024.</p>
      <div class="social"><i></i><i></i><i></i></div>
      <div class="col" style="left:108px"><b>Quick Links</b>Browse Collection<br>Sell Your Cars<br>Trade Portal<br>Community Forum<br>Newsletter</div>
      <div class="col" style="left:205px"><b>Resources</b>FAQ<br>Contact Support<br>Terms of Service<br>Privacy Policy<br>Grading Guide</div>
      <div class="a" style="left:302px;top:28px;font-size:3.8px;font-weight:600">Join the Mailing List</div>
      <div class="mail"><p class="small">Receive weekly rare find alerts and community auction highlights.</p><div class="field">email@address.com</div><span class="go"></span></div>
      <div class="bottom"><span>© 2026 Brimble Diecast. Your Marketplace for Miniature Masterpieces.</span><span>LONDON &nbsp;•&nbsp; TOKYO &nbsp;•&nbsp; NEW YORK</span></div>
    </footer>
  </section>

  <!-- PRODUCT DETAIL -->
  <section class="page" style="left:1385px;height:822px">
    <nav class="nav"><span class="brand">Brimble</span><div class="links"><span>Marketplace</span><span>Sell &amp; Trade</span><span>Community</span></div><div class="search">Search models...</div><div class="icons"><i></i><i style="border-radius:50%"></i></div><div class="cta">List Your Car</div></nav>
    <div class="a small" style="left:30px;top:54px;font-size:3px">CATALOG › AURELIO › CORSA 300 1962</div>
    <div class="photo" role="img" aria-label="Red classic racing coupe model on a grey backdrop" style="left:30px;top:73px;width:132px;height:122px;background:radial-gradient(ellipse at 50% 62%,#c21f1f 0 20%,#6c6f72 45%,#2d2f31)"><span class="badge a" style="left:6px;top:5px;background:var(--rust);color:#fff">MINT IN BOX</span><span class="badge a" style="left:6px;top:14px;background:#555;color:#fff">SCALE 1:12</span></div>
    <div class="photo ph-gray" role="img" aria-label="Interior detail view" style="left:30px;top:220px;width:30px;height:25px;border:1px solid var(--rust)"></div>
    <div class="photo ph-classic" role="img" aria-label="Front view" style="left:64px;top:220px;width:30px;height:25px"></div>
    <div class="photo ph-red" role="img" aria-label="Side view" style="left:98px;top:220px;width:30px;height:25px"></div>
    <div class="photo ph-studio" role="img" aria-label="Engine detail view" style="left:132px;top:220px;width:30px;height:25px"></div>

    <div class="a label" style="left:235px;top:74px">Quillon Collection</div>
    <h1 class="a" style="left:235px;top:82px;font-size:10px;font-weight:700;letter-spacing:-.3px">1962 Aurelio Corsa 300</h1>
    <div class="a" style="left:235px;top:105px;font-size:7px;font-weight:500">$14,250 <span class="small" style="font-size:3px">&nbsp; Free Insured Shipping</span></div>
    <div class="chip" style="left:235px;top:135px"><i></i><span>SCALE<br><b>1:12 Model</b></span></div>
    <div class="chip" style="left:280px;top:135px"><i style="border-radius:50%"></i><span>CONDITION<br><b>Mint in Box</b></span></div>
    <div class="chip" style="left:235px;top:157px"><i></i><span>SKU<br><b>AC-300-62A</b></span></div>
    <div class="a" style="left:235px;top:192px;width:129px;height:16px;border-radius:8px;background:linear-gradient(90deg,var(--rust),var(--orange));color:#fff;font-size:3.6px;text-align:center;padding-top:3px;font-weight:600;line-height:1.3">Buy<br>Now</div>
    <div class="a" style="left:235px;top:214px;width:129px;font-size:3.3px;display:flex;justify-content:space-around"><span>◇ Make Offer</span><span>⇄ Trade</span></div>
    <div class="a" style="left:235px;top:240px;width:129px;height:30px;background:var(--ivory);border-radius:3px"></div>
    <div class="a" style="left:242px;top:248px;width:13px;height:13px;border-radius:50%;background:#3a3633" role="img" aria-label="Seller avatar"></div>
    <div class="a" style="left:259px;top:249px;font-size:3.6px;font-weight:600">Castellan Classics<div class="small" style="font-size:2.8px;font-weight:400">★ 4.9 · 312 sales</div></div>
    <div class="a" style="left:340px;top:253px;font-size:3px;color:var(--rust);font-weight:600">Message</div>

    <div class="a" style="left:30px;top:296px;width:333px;border-bottom:.6px solid var(--line);display:flex;gap:22px;font-size:4.6px;color:var(--muted);padding-bottom:3px"><span style="color:var(--ink);font-weight:600;border-bottom:1px solid var(--rust);padding-bottom:2px">Description</span><span>Technical Specs</span><span>Provenance</span></div>
    <p class="a txt" style="left:30px;top:318px;width:250px;font-size:4.2px;color:#444">This Quillon Collection model is a masterpiece of miniature engineering. Created at 1:12 scale, it represents the 1962 Aurelio Corsa 300 precisely as it was driven by Edwin Harrow at the 1962 Ashcombe Tourist Trophy.</p>
    <p class="a small" style="left:30px;top:352px;width:250px">Hand-crafted using thousands of precision-engineered parts including cast metal, photo-etched stainless steel, and high-quality resin. The cockpit is a symphony of period-correct textures, featuring real leather seats with diamond-quilted detailing and a wood-rimmed steering wheel.</p>
    <div class="a small" style="left:35px;top:386px;width:60px;color:#333">✓ Limited Edition No. 14 of only 199 pieces worldwide.</div>
    <div class="a small" style="left:162px;top:386px;width:70px;color:#333">✓ Official Licensed Product with certificate.</div>

    <h2 class="a" style="left:30px;top:442px;font-size:8px;font-weight:500">You May Also Value</h2>
    <div class="photo ph-wood" role="img" aria-label="Silver classic sports car model on a wooden shelf" style="left:30px;top:463px;width:105px;height:132px;border-radius:2px"></div>
    <div class="photo ph-engine" role="img" aria-label="Silver engine block model" style="left:145px;top:463px;width:105px;height:132px;border-radius:2px"></div>
    <div class="photo ph-green" role="img" aria-label="Dark green classic roadster model" style="left:258px;top:463px;width:105px;height:132px;border-radius:2px"></div>
    <div class="a" style="left:30px;top:600px"><div style="font-size:5px;font-weight:600">Hollis Sprint RS</div><div class="small" style="font-size:3px">1:18 · Fenwick Models</div><div class="price" style="font-size:7px;margin-top:3px">$2,400</div></div>
    <div class="a" style="left:145px;top:600px"><div style="font-size:5px;font-weight:600">Halden Arrow 54</div><div class="small" style="font-size:3px">1:12 · Quillon</div><div class="price" style="font-size:7px;margin-top:3px">$12,800</div></div>
    <div class="a" style="left:258px;top:600px"><div style="font-size:5px;font-weight:600">Wexford Roadster S1</div><div class="small" style="font-size:3px">1:18 · Saraku</div><div class="price" style="font-size:7px;margin-top:3px">$450</div></div>

    <footer class="footer" style="top:670px">
      <div class="logo"><span></span>Brimble Diecast</div>
      <p class="about small">Your Marketplace for Miniature Masterpieces. Connecting collectors across the globe since 2024.</p>
      <div class="social"><i></i><i></i><i></i></div>
      <div class="col" style="left:108px"><b>Quick Links</b>Browse Collection<br>Sell Your Cars<br>Trade Portal<br>Community Forum<br>Newsletter</div>
      <div class="col" style="left:205px"><b>Resources</b>FAQ<br>Contact Support<br>Terms of Service<br>Privacy Policy<br>Grading Guide</div>
      <div class="a" style="left:302px;top:28px;font-size:3.8px;font-weight:600">Join the Mailing List</div>
      <div class="mail"><p class="small">Receive weekly rare find alerts and community auction highlights.</p><div class="field">email@address.com</div><span class="go"></span></div>
      <div class="bottom"><span>© 2026 Brimble Diecast. Your Marketplace for Miniature Masterpieces.</span><span>LONDON &nbsp;•&nbsp; TOKYO &nbsp;•&nbsp; NEW YORK</span></div>
    </footer>
  </section>

</div>
</body>
</html>
```